Consumer and commercial IOT solutions (Internet Of Things)

We are a startup and are looking for business cards with logo. The logo will appear on all of our media as well as our ecommerce site and social sites that have yet to be developed. We want to present a fresh face on a high tech company that innovates at every turn. You can read about our solutions on our information only web site www.plorbaxsystems.net - We have some wording we would like used on our business cards but there is no place for this except for here. The company name is "RM Industrial IOT" I have some samples of logos I am interested in seeing but I will let your team make the initial presentations

```html
<!DOCTYPE html>
<html lang="en">
<head>
<meta charset="utf-8">
<title>RM Industrial IOT – Business Card</title>
<link rel="stylesheet" href="https://fonts.googleapis.com/css2?family=Lato:wght@400;700&family=PT+Sans:wght@700&family=Questrial&family=Ubuntu:wght@700&display=swap">
<style>
  :root {
    --brand-blue: #0a8fcf;
    --brand-deep: #0093d6;
    --brand-mid: #00a6cb;
    --brand-teal: #4ab2bf;
    --name-blue: #1a6fb0;
    --icon-blue: #13a0d2;
    --ink: #2b2b2b;
    --rule: #8c8c8c;
    --card-border: #a8a8a8;
    --paper: #ffffff;
  }
  * { margin: 0; padding: 0; box-sizing: border-box; }
  html, body { width: 872px; height: 1200px; overflow: hidden; background: var(--paper); }
  .sheet { position: relative; width: 872px; height: 1200px; }

  .brand {
    position: absolute;
    display: flex; align-items: center; gap: 10px;
    font-family: "Ubuntu", sans-serif; font-weight: 700;
    letter-spacing: 0.5px; white-space: nowrap;
  }
  .brand-dot { width: 14px; height: 14px; border-radius: 50%; background: currentColor; flex: none; }

  .brand--hero { left: 0; width: 872px; justify-content: center; top: 170px; font-size: 31px; color: var(--brand-blue); }

  .side-label {
    position: absolute; left: 0; width: 872px; text-align: center;
    font-family: "Questrial", sans-serif; font-size: 29px; color: #222;
  }
  .side-label--back { top: 336px; }
  .side-label--front { top: 749px; }

  .card { position: absolute; left: 110px; width: 648px; height: 365px; }
  .card--back {
    top: 379px;
    background: linear-gradient(32deg, var(--brand-deep) 0%, var(--brand-deep) 30%, var(--brand-mid) 58%, var(--brand-teal) 64%, var(--brand-teal) 100%);
  }
  .card--back .brand { left: 0; width: 648px; justify-content: center; top: 165px; font-size: 27px; color: var(--paper); }

  .card--front { top: 788px; background: var(--paper); border: 1px solid var(--card-border); }
  .card--front .brand { left: 38px; top: 160px; font-size: 21px; color: var(--brand-blue); gap: 7px; }
  .card--front .brand-dot { width: 11px; height: 11px; }

  .divider { position: absolute; left: 276px; top: 70px; width: 1.5px; height: 224px; background: var(--rule); }

  .person-name {
    position: absolute; left: 293px; top: 80px;
    font-family: "PT Sans", sans-serif; font-weight: 700; font-size: 27px; color: var(--name-blue);
  }
  .contact-list { position: absolute; left: 293px; top: 131px; list-style: none;
    font-family: "Lato", sans-serif; font-size: 21px; color: var(--ink); line-height: 27px; }
  .contact-list li { display: flex; align-items: flex-start; margin-bottom: 4px; }
  .contact-list svg { width: 18px; height: 18px; margin: 4px 18px 0 0; flex: none; }
  .contact-list .address span { display: block; }
</style>
</head>
<body>
<main class="sheet">
  <div class="brand brand--hero"><span class="brand-dot"></span>RM INDUSTRIAL IOT</div>

  <p class="side-label side-label--back">Back side</p>
  <section class="card card--back" aria-label="Card back">
    <div class="brand"><span class="brand-dot"></span>RM INDUSTRIAL IOT</div>
  </section>

  <p class="side-label side-label--front">Front side</p>
  <section class="card card--front" aria-label="Card front">
    <div class="brand"><span class="brand-dot"></span>RM INDUSTRIAL IOT</div>
    <div class="divider"></div>
    <h1 class="person-name">Person Name</h1>
    <ul class="contact-list">
      <li>
        <svg viewBox="0 0 18 18" fill="none" stroke="var(--icon-blue)" stroke-width="2"><rect x="4" y="1" width="10" height="16" rx="2"/><circle cx="9" cy="13.5" r="0.8" fill="var(--icon-blue)"/></svg>
        123.4567.8900
      </li>
      <li>
        <svg viewBox="0 0 18 18" fill="none" stroke="var(--icon-blue)" stroke-width="1.6"><circle cx="9" cy="9" r="7.5"/><ellipse cx="9" cy="9" rx="3.2" ry="7.5"/><path d="M1.5 9h15M3 5h12M3 13h12"/></svg>
        www.rmindustrialiot.net
      </li>
      <li>
        <svg viewBox="0 0 18 18" fill="none" stroke="var(--icon-blue)" stroke-width="1.6"><rect x="1" y="4" width="16" height="11" fill="var(--icon-blue)"/><path d="M1 4l8 6 8-6M1 15l6-5M17 15l-6-5" stroke="#fff"/></svg>
        hello@rmindustrialiot.net
      </li>
      <li class="address">
        <svg viewBox="0 0 18 18"><path d="M9 1a5.5 5.5 0 0 0-5.5 5.5C3.5 11 9 17 9 17s5.5-6 5.5-10.5A5.5 5.5 0 0 0 9 1z" fill="var(--icon-blue)"/><circle cx="9" cy="6.5" r="2" fill="#fff"/></svg>
        <div><span>240 Harbor Lane</span><span>Millbrook, NY 12545</span></div>
      </li>
    </ul>
  </section>
</main>
</body>
</html>
```